Restaurant Menu for beach club in Martinique

We would like to set a new design for our Menu. We are a restaurant, and beach club, located in Martinique. Our website is available at : http://www.korivagueplage.net Regards

Colors

Designer to choose colors to be used in the design.

```html
<!DOCTYPE html>
<html lang="fr">
<head>
<meta charset="utf-8">
<title>Kori Vague – Menu</title>
<link rel="stylesheet" href="https://fonts.googleapis.com/css2?family=Almendra+SC&family=Arimo:wght@600;700&family=Work+Sans:ital,wght@0,400;1,400&display=swap">
<style>
  :root {
    --stage: #e7e3da;
    --teal: #1b9bb0;
    --sage: #98b09b;
    --sand: #dcc28a;
    --bark: #74482a;
    --title: #6d4424;
    --copy: #6a4a30;
    --ink: #1f1a14;
  }
  * { box-sizing: border-box; margin: 0; padding: 0; }
  html, body {
    width: 1200px; height: 1200px; overflow: hidden;
    background: var(--stage);
  }
  .menu {
    position: absolute; left: 200px; top: 32px;
    width: 801px; height: 1135px;
    background: repeating-linear-gradient(90deg, var(--teal) 0 58px, var(--sage) 58px 116px);
    box-shadow: 0 6px 18px rgba(0,0,0,.18);
  }
  .menu__side {
    position: absolute; top: 0; width: 37px; height: 100%;
    background: repeating-linear-gradient(180deg, var(--teal) 0 58px, var(--sage) 58px 116px);
  }
  .menu__side--left { left: 0; }
  .menu__side--right { right: 0; }
  .menu__panel { position: absolute; left: 0; top: 0; width: 801px; height: 1135px; }
  .brand {
    position: absolute; left: 74px; top: 80px; width: 300px;
    text-align: center;
    font-family: "Arimo", sans-serif; font-weight: 700;
    font-size: 34px; letter-spacing: 3px; color: var(--title);
  }
  .section-title {
    position: absolute; text-align: center;
    font-family: "Almendra SC", serif; font-size: 40px;
    color: var(--ink); letter-spacing: 2px; line-height: 1;
  }
  .col-left { left: 74px; width: 300px; }
  .col-right { left: 413px; width: 330px; }
  .dish { position: absolute; text-align: center; }
  .dish__name {
    font-family: "Arimo", sans-serif; font-weight: 700;
    font-size: 19.5px; line-height: 22px; color: var(--title);
  }
  .dish__desc {
    margin-top: 6px;
    font-family: "Work Sans", sans-serif; font-size: 12.5px;
    letter-spacing: 1px; line-height: 17.5px; color: var(--copy);
  }
  .dish__price {
    margin-top: var(--gap, 20px);
    font-family: "Arimo", sans-serif; font-weight: 700;
    font-size: 18px; line-height: 22px; color: var(--ink);
  }
  .palms {
    position: absolute; left: 58px; top: 865px; width: 315px; height: 200px;
    background: radial-gradient(ellipse at 50% 60%, #7a4a27 0%, #8a5a33 45%, rgba(138,90,51,0) 72%);
    opacity: .85;
  }
  .note {
    position: absolute; right: 98px; top: 1076px;
    font-family: "Work Sans", sans-serif; font-style: italic;
    font-size: 9.5px; letter-spacing: .4px; color: var(--copy);
  }
</style>
</head>
<body>
<div class="menu">
  <div class="menu__side menu__side--left"></div>
  <div class="menu__side menu__side--right"></div>

  <svg class="menu__panel" viewBox="0 0 801 1135" aria-hidden="true">
    <path d="M74 30 H727 A37 37 0 0 0 764 67 V1072 A37 37 0 0 0 727 1109 H74 A37 37 0 0 0 37 1072 V67 A37 37 0 0 0 74 30 Z" fill="#dcc28a"/>
    <path d="M80 36 H721 A37 37 0 0 0 758 73 V1066 A37 37 0 0 0 721 1103 H80 A37 37 0 0 0 43 1066 V73 A37 37 0 0 0 80 36 Z" fill="none" stroke="#74482a" stroke-width="2.5" stroke-dasharray="9 5"/>
    <line x1="401" y1="99" x2="401" y2="1044" stroke="#74482a" stroke-width="1.2" stroke-dasharray="12 10"/>
  </svg>

  <div class="brand">KORI VAGUE</div>

  <h2 class="section-title col-left" style="top:198px">ENTRÉES</h2>

  <div class="dish col-left" style="top:259px">
    <p class="dish__name">L’ASSIETTE «ZEN»</p>
    <p class="dish__desc">(nem de gambas, maki au saumon,<br>mini brochette de poulet, samoussa au<br>chèvre frais)</p>
    <p class="dish__price" style="--gap:15px">9,80 €</p>
  </div>
  <div class="dish col-left" style="top:394px">
    <p class="dish__name">LES NEMS AUX DEUX SAUMONS</p>
    <p class="dish__desc">sauce crémeuse au wasabi et salade<br>de pousses d’épinards</p>
    <p class="dish__price" style="--gap:20px">9,50 €</p>
  </div>
  <div class="dish col-left" style="top:531px">
    <p class="dish__name">LA SALADE DU « PÉRIGORD »</p>
    <p class="dish__desc">(Salade, roquette, oignons rouges, foie<br>gras maison, gésiers confits, magrets<br>fumés et pommes)</p>
    <p class="dish__price" style="--gap:14px">13,10 €</p>
  </div>
  <div class="dish col-left" style="top:666px">
    <p class="dish__name">LE TARTARE DE LOUP</p>
    <p class="dish__desc">sur une gelée de concombres à la<br>moutarde de Reims</p>
    <p class="dish__price" style="--gap:16px">10,50 €</p>
  </div>
  <div class="dish col-left" style="top:789px">
    <p class="dish__name">LE BAVAROIS DE TOMATES</p>
    <p class="dish__desc">farci au chèvre frais et jus de betterave</p>
    <p class="dish__price" style="--gap:22px">8,20 €</p>
  </div>

  <div class="palms" role="img" aria-label="Illustration de deux palmiers sur le sable"></div>

  <h2 class="section-title col-right" style="top:72px">PLATS</h2>

  <div class="dish col-right" style="top:130px">
    <p class="dish__name">LE ROYAL DE FOIE GRAS</p>
    <p class="dish__desc">et rouleau de printemps au poulet et<br>vermicelles</p>
    <p class="dish__price" style="--gap:14px">10,50 €</p>
  </div>
  <div class="dish col-right" style="top:251px">
    <p class="dish__name">LE TARTARE DE ST JACQUES</p>
    <p class="dish__desc">aux échalotes rôties et concombres</p>
    <p class="dish__price" style="--gap:22px">12,50 €</p>
  </div>
  <div class="dish col-right" style="top:356px">
    <p class="dish__name">L’OEUF “COCOTTE”</p>
    <p class="dish__desc">à la crème de morilles et jambon<br>ibérique</p>
    <p class="dish__price" style="--gap:14px">9,50 €</p>
  </div>
  <div class="dish col-right" style="top:482px">
    <p class="dish__name">LA SALADE DE LÉGUMES</p>
    <p class="dish__desc">croquants et gambas façon thaï</p>
    <p class="dish__price" style="--gap:22px">9,80 €</p>
  </div>
  <div class="dish col-right" style="top:596px">
    <p class="dish__name">LE FOIE GRAS DE CANARD</p>
    <p class="dish__desc">au vieux porto, brioche maison</p>
    <p class="dish__price" style="--gap:22px">13,80 €</p>
  </div>
  <div class="dish col-right" style="top:706px">
    <p class="dish__name">LE GÂTEAU DE LAPEREAU</p>
    <p class="dish__desc">au lard paysan, farci au foie gras,<br>compote d’oignons rouges</p>
    <p class="dish__price" style="--gap:14px">9,80 €</p>
  </div>
  <div class="dish col-right" style="top:826px">
    <p class="dish__name">LA VERRINE</p>
    <p class="dish__desc">aux 3 choux-fleurs, crabe et saumon<br>fumé</p>
    <p class="dish__price" style="--gap:14px">11,50 €</p>
  </div>
  <div class="dish col-right" style="top:947px">
    <p class="dish__name">LE FOIE GRAS FRAIS</p>
    <p class="dish__desc">poêlé aux cèpes et son jus corsé de<br>canard</p>
    <p class="dish__price" style="--gap:14px">12,50 €</p>
  </div>

  <p class="note">Tous nos prix sont indiqués en TTC et comprennent la TVA a 5.5 %</p>
</div>
</body>
</html>
```